Pet Shop Website

website will need to have the following features:
• Photo Galleries of each species (Dogs, Cats, Birds, Fish, Reptiles, Rabbits) in a light box popup
o Each species may have several different categories for example:
 Fish
• Marine fish
• Fresh water
• tropical
• Cichlid
• Information Fact sheets of each species – Downloaded as a pdf which can be either
o Care Sheets
o Training Sheets
• Members Area
o Username (Email Address) & Password login
o New signups
o Exclusive Member Deals
o Newsletter options

The front page must be very simple (for example lumavest.com.au) contain the following:
• Product of the week - which can be purchased online
o Short details
o Cost
• Pet Club Sign up picture
• Animal of the week/month
• Contact Phone Number and addresses of the stores
• A jQuery slideshow (Images could include stores, pets etc…)
The main page MUST keep simple. We do not want it cluttered.

Inner Page
The animals / reptile page will need to have:
• Short description of the species
• Photo Galleries
• A list of what is in stock and the list needs to clearly be sorted by each store (Use of Tabs maybe).
• Facts sheets / Info sheets
The type of website ideas (not the type of look that we are necessary after) is and the sort of content that we want to offer are as follows:

http://www.scalenook.com.au/
http://www.brindlecovepaws.com.au/
http://www.thefurrowden.com.au
http://www.tailtown.net.au

Colour in the new website:
Blue
Red
Grey
Yellow

Original site:

http://www.critterglow.com.au
Updates

Hi Guys,

We had feedback from the client and they would like to see a few dark designs.

Thanks                                   

Reason: We would like to reopen this contest back up for a further week

Target Market(s)

Targeting animal lovers

Industry/Entity Type

Store

Requirements
Should not have
• Alter the logo in anyway

```html
<!DOCTYPE html>
<html lang="en">
<head>
<meta charset="utf-8">
<title>Critter Glow — Pet Store</title>
<link rel="stylesheet" href="https://fonts.googleapis.com/css2?family=Bree+Serif&family=Open+Sans:wght@400;600&display=swap">
<style>
:root{
  --blue:#1e2b9c;
  --blue-dark:#121c72;
  --blue-light:#3445c4;
  --yellow:#ffd21a;
  --red:#c8141c;
  --grey-bg:#eceeee;
  --grey-panel:#dcdcda;
  --footer:#2a2a2a;
  --footer-text:#8d8d8d;
  --white:#ffffff;
}
*{box-sizing:border-box;margin:0;padding:0}
html,body{width:907px;height:1200px;overflow:hidden}
body{position:relative;background:var(--grey-bg);font-family:"Open Sans",sans-serif;color:#333}
.sky{position:absolute;left:0;top:0;width:907px;height:420px;background:linear-gradient(#cfe0ec,#e8f0f4 60%,var(--grey-bg))}
.brand{position:absolute;left:45px;top:38px;display:flex;align-items:center;gap:10px;font-family:"Bree Serif",serif;font-size:30px;color:var(--blue)}
.brand .mark{width:18px;height:18px;background:var(--yellow)}
.auth{position:absolute;top:40px;display:flex;gap:10px;right:22px}
.auth a{display:block;padding:3px 6px;font-family:"Bree Serif",serif;font-size:14px;color:#fff;text-decoration:none;background:linear-gradient(var(--blue-light),var(--blue-dark));border:2px solid #fff;border-radius:5px;box-shadow:0 1px 3px rgba(0,0,0,.4)}
.nav{position:absolute;left:22px;top:117px;width:867px;height:43px;background:linear-gradient(var(--blue-light),var(--blue) 60%,var(--blue-dark));display:flex;align-items:center;padding-left:9px}
.nav a{font-family:"Bree Serif",serif;font-size:13px;color:#fff;text-decoration:none;padding:7px 14px;margin-right:10px}
.nav a.active{background:var(--yellow);color:var(--red);border:1px solid #e2a800}
.login-pop{position:absolute;left:655px;top:78px;width:185px;height:114px;background:#fff;border:1px solid #bbb;border-radius:3px;box-shadow:0 2px 6px rgba(0,0,0,.3);padding:15px 14px 0;z-index:3}
.login-pop .close{position:absolute;right:-6px;top:-6px;width:14px;height:14px;background:#999;color:#fff;font-size:10px;text-align:center;line-height:14px}
.login-pop .field{height:23px;border:1px solid var(--blue);background:#eef0fb;font-size:11px;font-weight:600;padding:3px 8px;margin-bottom:13px}
.login-pop .row{display:flex;justify-content:space-between;align-items:center;margin-top:-3px}
.login-pop .forgot{font-size:9px;color:var(--red)}
.login-pop .btn{background:linear-gradient(#ffe47a,#f0b000);font-size:12px;padding:1px 8px;border:1px solid #c89000}
.slider{position:absolute;left:27px;top:162px;width:857px;height:273px;background:#fff;padding:4px 9px 10px;box-shadow:0 1px 4px rgba(0,0,0,.25)}
.slider .photo{width:100%;height:100%;background:linear-gradient(90deg,#c0261b 0%,#e07a34 25%,#d9a45f 45%,#c99553 55%,#2d62c4 70%,#e9502a 80%,#f1c22a 100%)}
.slider h1{position:absolute;left:0;right:0;top:16px;text-align:center;font-family:"Bree Serif",serif;font-weight:400;font-size:34px;color:#fff;letter-spacing:1px}
.dots{position:absolute;left:406px;top:452px;display:flex;gap:6px}
.dots span{width:10px;height:10px;border-radius:50%;background:#777;border:1px solid #555}
.dots span.on{background:var(--blue)}
.card{position:absolute;top:486px;width:266px;height:208px}
.card h2{height:44px;background:linear-gradient(var(--blue-light),var(--blue) 60%,var(--blue-dark));font-family:"Bree Serif",serif;font-weight:400;font-size:17px;color:#fff;padding:11px 16px}
.card .body{position:relative;margin:0 4px;height:164px;background:#fff;padding:0 4px 4px;box-shadow:0 1px 3px rgba(0,0,0,.3)}
.card .pic{height:160px}
.card .more{position:absolute;right:4px;bottom:4px;background:var(--yellow);color:var(--red);font-size:11px;padding:2px 7px}
.newsletter .body{background:linear-gradient(#9ac4d6,#6fa0b5);padding:6px 6px}
.newsletter p{font-size:10px;color:#223;line-height:1.5}
.newsletter .box{position:absolute;left:16px;bottom:22px;width:248px;height:68px;background:rgba(90,100,110,.75);border-radius:8px;padding:8px}
.newsletter .in{width:135px;height:20px;background:#fff;border:1px solid #999;font-size:9px;padding:3px 6px;margin-bottom:9px}
.newsletter .reg{position:absolute;right:14px;top:30px;background:linear-gradient(#e23a3a,#a50d12);color:#fff;font-size:11px;font-weight:600;padding:3px 7px;border:1px solid #fff}
.gallery{position:absolute;left:14px;top:755px;width:880px;height:276px;background:var(--grey-panel);border:1px solid #ccc;border-radius:6px}
.gallery-tab{position:absolute;left:0;top:724px;width:907px;height:40px;z-index:1}
.gallery-title{position:absolute;left:0;right:0;top:736px;text-align:center;font-family:"Bree Serif",serif;font-weight:400;font-size:22px;line-height:26px;color:#8a8a8a;letter-spacing:2px;z-index:2}
.gallery .well{position:absolute;left:7px;top:23px;width:866px;height:245px;border-radius:6px;background:#c8c2b6 radial-gradient(#b3ac9f 1px,transparent 1.5px) 0 0/6px 6px}
.item{position:absolute;top:795px;width:162px;height:214px;background:#eee;border:1px solid #ccc;padding:7px;text-align:center;font-size:11px;color:#333}
.item .pic{height:146px;background:#fff}
.item .name{margin-top:12px}
.item .price{margin-top:12px}
.arrow{position:absolute;top:876px;width:34px;height:46px;background:#eee;border-radius:50%;display:flex;align-items:center;justify-content:center;box-shadow:0 1px 3px rgba(0,0,0,.3)}
.footer{position:absolute;left:0;top:1073px;width:907px;height:127px;background:var(--footer)}
.footer .zig{position:absolute;left:0;top:-8px}
.footer .brand-foot{position:absolute;left:28px;top:32px;display:flex;align-items:center;gap:8px;font-family:"Bree Serif",serif;font-size:20px;color:#bbb}
.footer .brand-foot .mark{width:12px;height:12px;background:#bbb}
.footer .copy{position:absolute;left:26px;top:92px;font-size:12px;color:var(--footer-text)}
.social{position:absolute;left:306px;top:20px;display:grid;grid-template-columns:20px 20px;gap:10px 14px}
.social span{width:20px;height:20px;border-radius:50%;background:#4a4a4a}
.foot-nav{position:absolute;left:414px;top:22px;display:flex;flex-direction:column;gap:9px}
.foot-nav a{font-family:"Bree Serif",serif;font-size:12px;color:#ddd;text-decoration:none}
.stores h3{position:absolute;left:543px;top:14px;font-family:"Bree Serif",serif;font-size:30px;color:#3a3a3a;letter-spacing:2px;font-weight:400}
.store{position:absolute;top:52px;font-size:12px;line-height:1.35;color:var(--footer-text)}
.store b{color:#ccc;font-weight:600}
.store.second{left:734px;font-size:11px}
.store.first{left:543px}
.divider{position:absolute;left:712px;top:60px;width:1px;height:60px;background:#444}
</style>
</head>
<body>
<div class="sky"></div>

<header>
  <div class="brand"><span class="mark"></span>Critter Glow</div>
  <nav class="auth"><a href="#">Login</a><a href="#">Sign Up</a></nav>
  <nav class="nav">
    <a href="#" class="active">HOME</a><a href="#">ABOUT</a><a href="#">PETS</a><a href="#">CONTACT</a>
  </nav>
  <form class="login-pop">
    <span class="close">X</span>
    <div class="field">Password:</div>
    <div class="field">User Name:</div>
    <div class="row"><span class="forgot">Forget Password?</span><span class="btn">Login</span></div>
  </form>
</header>

<section class="slider">
  <div class="photo" role="img" aria-label="Slideshow photo of a parrot, kittens, a puppy, fish and parakeets"></div>
  <h1>CRITTER GLOW STORE</h1>
</section>
<div class="dots"><span></span><span class="on"></span><span></span><span></span></div>

<section class="card" style="left:23px">
  <h2>Pet Club Sign up</h2>
  <div class="body"><div class="pic" role="img" aria-label="Group photo of dogs, cats and a parrot" style="background:linear-gradient(135deg,#6b3a24,#c98a4c 50%,#e7d6b8)"></div><span class="more">Read more</span></div>
</section>
<section class="card" style="left:325px">
  <h2>Animal of the week/month</h2>
  <div class="body"><div class="pic" role="img" aria-label="Photo of a spaniel puppy" style="background:radial-gradient(circle at 50% 55%,#a2521e,#c77a3c 45%,#fff 75%)"></div><span class="more">Read more</span></div>
</section>
<section class="card newsletter" style="left:621px">
  <h2>Signup to our Newsletter</h2>
  <div class="body">
    <p>Stay up to date with in-store specials by joining our newsletter</p>
    <form class="box">
      <div class="in">Name:</div>
      <div class="in">Email:</div>
      <span class="reg">Register</span>
    </form>
  </div>
</section>

<section class="gallery"><div class="well"></div></section>
<svg class="gallery-tab" width="907" height="40" viewBox="0 0 907 40" aria-hidden="true">
  <path d="M15 31 H230 C300 31 330 2 380 2 H527 C577 2 607 31 677 31 H893 V40 H15 Z" fill="#dcdcda"/>
  <path d="M15 31 H230 C300 31 330 2 380 2 H527 C577 2 607 31 677 31 H893" fill="none" stroke="#ccc"/>
</svg>
<h2 class="gallery-title">GALLERY</h2>

<article class="item" style="left:72px"><div class="pic" role="img" aria-label="Puppy with a bowl of food" style="background:radial-gradient(circle,#d49a4e 30%,#fff 65%)"></div><p class="name">Chihuahua X Jack Russell</p><p class="price">$ 795.00</p></article>
<article class="item" style="left:274px"><div class="pic" role="img" aria-label="Ginger cat" style="background:radial-gradient(circle,#d48d4f 28%,#fff 62%)"></div><p class="name">Chihuahua X Jack Russell</p><p class="price">$ 795.00</p></article>
<article class="item" style="left:476px"><div class="pic" role="img" aria-label="Rainbow lorikeet" style="background:radial-gradient(circle,#3a7a3a,#e36b1f 30%,#fff 62%)"></div><p class="name">Chihuahua X Jack Russell</p><p class="price">$ 795.00</p></article>
<article class="item" style="left:686px"><div class="pic" role="img" aria-label="Rabbit" style="background:radial-gradient(circle,#d9a56a 28%,#fff 62%)"></div><p class="name">Chihuahua X Jack Russell</p><p class="price">$ 795.00</p></article>

<div class="arrow" style="left:14px"><svg width="10" height="14"><path d="M8 1 L2 7 L8 13" fill="none" stroke="#888" stroke-width="2"/></svg></div>
<div class="arrow" style="left:859px"><svg width="10" height="14"><path d="M2 1 L8 7 L2 13" fill="none" stroke="#888" stroke-width="2"/></svg></div>

<footer class="footer">
  <svg class="zig" width="907" height="9" aria-hidden="true"><defs><pattern id="zig" width="8" height="9" patternUnits="userSpaceOnUse"><path d="M0 9 L4 1 L8 9 Z" fill="#2a2a2a"/></pattern></defs><rect width="907" height="9" fill="url(#zig)"/></svg>
  <div class="brand-foot"><span class="mark"></span>Critter Glow</div>
  <p class="copy">©2012-2013 Critter Glow. All rights reserved.</p>
  <div class="social"><span></span><span></span><span></span><span></span><span></span><span></span></div>
  <nav class="foot-nav"><a href="#">HOME</a><a href="#">ABOUT US</a><a href="#">PETS</a><a href="#">CONTACT US</a></nav>
  <div class="stores">
    <h3>STORE LOCATIONS</h3>
    <p class="store first">Shop 4 / 820 Harbour Rd<br>MARLOWE W.A 6109<br><b>Phone:</b> (08) 9000 1234<br><b>Fax:</b> (08) 9000 1235</p>
    <span class="divider"></span>
    <p class="store second">Unit 3 / 22 Beacon Drive<br>ASHGROVE W.A 6165<br><b>Phone:</b> (08) 9000 5678<br><b>Fax:</b> (08) 9000 5679</p>
  </div>
</footer>
</body>
</html>
```